flyer for a plumbing company in california

i need a flyer to promote trench-less services Pipe Install,Replacements & enlargements to other local plumbing compare owners.
Updates

the graphics that i submitted where pulled from internet just as an example, i would need graphics that a can legally use. thanks for the designs,

hello, i uploaded files for this project, thanks for your work....

Target Market(s)

other local plumbing company owners

Industry/Entity Type

Plumber

Colors
ec1f27
0356a4

Requirements
Must have
• a sample for showing prices
• a clear message that this services are special for only other local plumbing companies.
• Pierce ,Pull and Go.
• New Installs, Pipe Replacements & Enlarge
• —Sewer Lateral 3”-6”
• — Water Service 3/4”-6”
• —Gas 3/4”-6”
• —Electrical Conduit 3/4”-6”
• —Vacumm 2”-6”
• call for a free consultation 530 812-3097
Nice to have
• "Unique Graphics"
• First Step: The piercing tool launching cradle is adjusted to a Realistic desired grade/slop to create a new bore axis.
• Second Step: A new 3-6’ polly sewer pipe rated to last more than 20 years is pulled
• Operator & Trenchless Equipment Rental.
• —Pipe Fuser 2”-6”
• —Pipe Burster Stone Viper KT72
• —Hydro power pack 13 PSI 3,000
• —2” Stoneviper Mole
Should not have
• any underline words.

```html
<!DOCTYPE html>
<html lang="en">
<head>
<meta charset="utf-8">
<title>Trenchless Services Flyer</title>
<link rel="stylesheet" href="https://fonts.googleapis.com/css2?family=Lato:wght@300;400;700;900&family=Arimo:wght@400;700&display=swap">
<style>
  :root {
    --brand-red: #d9262c;
    --band-grey: #7b7870;
    --text-grey: #8a8782;
    --rule-grey: #dcd9d3;
    --ink: #222222;
    --white: #ffffff;
    --frame-red: #e8666a;
  }
  * { margin: 0; padding: 0; box-sizing: border-box; }
  html, body { width: 974px; height: 1200px; overflow: hidden; background: var(--white); }
  .flyer { position: relative; width: 974px; height: 1200px; overflow: hidden; font-family: "Lato", sans-serif; background: var(--white); }

  .hero-photo {
    position: absolute; left: 0; top: 0; width: 974px; height: 478px;
    background: linear-gradient(180deg, #8a8f86 0%, #6f6a55 22%, #7d5a3f 40%, #4d6b34 58%, #3f7a2a 100%);
  }
  .hero-text { position: absolute; left: 36px; top: 38px; color: var(--white); text-shadow: 0 1px 3px rgba(0,0,0,.35); }
  .eyebrow { font-weight: 400; font-size: 31px; line-height: 1; }
  .headline { font-weight: 900; font-size: 52px; line-height: 54px; margin-top: 6px; letter-spacing: -0.3px; }
  .tagline { font-weight: 400; font-size: 22px; margin-top: 12px; }
  .intro { font-weight: 400; font-size: 18px; line-height: 27px; margin-top: 18px; }

  .rental-band { position: absolute; left: 0; top: 478px; width: 974px; height: 236px; background: var(--band-grey); }
  .rental-title { position: absolute; left: 36px; top: 22px; color: var(--white); font-weight: 700; font-size: 27px; line-height: 33px; }
  .rental-list { position: absolute; left: 36px; top: 112px; list-style: none; color: var(--white); font-family: "Arimo", sans-serif; font-weight: 700; font-size: 16.5px; line-height: 26px; }

  .equipment-photo { position: absolute; left: 0; top: 0; }

  .services { position: absolute; left: 36px; top: 724px; width: 440px; }
  .services-title { color: var(--brand-red); font-weight: 900; font-size: 29px; line-height: 36px; }
  .services-copy { color: var(--text-grey); font-family: "Arimo", sans-serif; font-weight: 700; font-size: 17.5px; line-height: 25px; margin-top: 4px; }
  .trade-notice { margin-top: 8px; color: var(--brand-red); font-family: "Arimo", sans-serif; font-weight: 700; font-size: 13px; line-height: 16px; }

  .price-table { margin-top: 6px; width: 430px; border-collapse: collapse; font-family: "Arimo", sans-serif; font-size: 12.5px; line-height: 16px; color: var(--ink); }
  .price-table caption { text-align: left; font-weight: 700; font-size: 13px; color: var(--band-grey); padding-bottom: 2px; }
  .price-table td { padding: 1px 0; border-bottom: 1px solid var(--rule-grey); }
  .price-table .size { color: var(--text-grey); }
  .price-table .price { text-align: right; font-weight: 700; color: var(--brand-red); }

  .brand { position: absolute; left: 36px; top: 1020px; display: flex; align-items: center; gap: 12px; }
  .brand-mark { width: 34px; height: 34px; background: var(--brand-red); }
  .brand-name { font-weight: 900; font-size: 38px; color: var(--band-grey); }

  .contact { position: absolute; left: 36px; top: 1096px; }
  .contact-label { color: var(--text-grey); font-weight: 300; font-size: 20px; }
  .contact-phone { color: var(--brand-red); font-weight: 900; font-size: 32px; margin-top: 2px; }

  .step-figure { position: absolute; left: 539px; width: 389px; border: 1.5px solid var(--frame-red); background: linear-gradient(180deg, #ffffff 0%, #eef3ea 55%, #e3ddd2 100%); }
  .step-one { top: 744px; height: 167px; }
  .step-two { top: 966px; height: 161px; }
  .step-caption { position: absolute; left: 539px; width: 400px; font-family: "Arimo", sans-serif; font-weight: 700; font-size: 12px; line-height: 15px; color: var(--ink); white-space: nowrap; }
  .step-caption b { color: var(--brand-red); }
  .step-caption .indent { padding-left: 44px; }
  .caption-one { top: 926px; }
  .caption-two { top: 1142px; }
</style>
</head>
<body>
<div class="flyer">
  <div class="hero-photo" role="img" aria-label="Photo of a brick manor house behind a wide green lawn and trees"></div>

  <div class="hero-text">
    <p class="eyebrow">Fellow Plumbers</p>
    <h1 class="headline">WHY DESTROYING A<br>BEAUTIFULL LANDSCAPE</h1>
    <p class="tagline">Minimal Digging, Minimal Damage to Landscape</p>
    <p class="intro">With the powerful and robust pulling rigs,<br>damaged old pipes can be renewed<br>without the need for trenches.</p>
  </div>

  <section class="rental-band">
    <h2 class="rental-title">Operator &amp; Trenchless<br>Equipment Rental.</h2>
    <ul class="rental-list">
      <li>Pipe Fuser 2”-6”</li>
      <li>Pipe Burster Stone Viper KT72</li>
      <li>Hydro power pack 13 PSI 3,000</li>
      <li>2” Stoneviper Mole</li>
    </ul>
  </section>

  <svg class="equipment-photo" width="974" height="720" viewBox="0 0 974 720" role="img" aria-label="Photo of a red and black trenchless pipe bursting rig on its launch frame">
    <defs>
      <linearGradient id="rigTone" x1="0" y1="0" x2="1" y2="1">
        <stop offset="0" stop-color="#c62128"/>
        <stop offset="0.45" stop-color="#2a2a2a"/>
        <stop offset="1" stop-color="#111111"/>
      </linearGradient>
    </defs>
    <polygon points="720,320 880,300 935,560 930,690 330,690 330,480 620,440" fill="url(#rigTone)" opacity="0.92"/>
  </svg>

  <section class="services">
    <h2 class="services-title">PIERCE, PULL AND GO.</h2>
    <p class="services-copy">Our trenchless pipe lining services are<br>designed to meet the highest standards of<br>efficiency, excellence and quality.</p>
    <p class="trade-notice">Trade rates offered only to local plumbing companies.</p>
    <table class="price-table">
      <caption>New Installs, Pipe Replacements &amp; Enlarge</caption>
      <tr><td>Sewer Lateral</td><td class="size">3”-6”</td><td class="price">from $48 / ft</td></tr>
      <tr><td>Water Service</td><td class="size">3/4”-6”</td><td class="price">from $36 / ft</td></tr>
      <tr><td>Gas</td><td class="size">3/4”-6”</td><td class="price">from $40 / ft</td></tr>
      <tr><td>Electrical Conduit</td><td class="size">3/4”-6”</td><td class="price">from $32 / ft</td></tr>
      <tr><td>Vacumm</td><td class="size">2”-6”</td><td class="price">from $30 / ft</td></tr>
    </table>
  </section>

  <div class="brand">
    <span class="brand-name">Sierra Line Plumbing</span>
    <span class="brand-mark"></span>
  </div>

  <div class="contact">
    <p class="contact-label">Call for a free consultation</p>
    <p class="contact-phone">530 812-3097</p>
  </div>

  <div class="step-figure step-one" role="img" aria-label="Diagram of a worker setting the piercing tool launch cradle with line of sight to the exit pit"></div>
  <p class="step-caption caption-one"><b>STEP 1:</b> The piercing tool launching cradle is adjusted to a<br><span class="indent">Realistic desired grade/slop to create a new bore axis.</span></p>

  <div class="step-figure step-two" role="img" aria-label="Diagram of a bursting head pulling a new pipe through the host pipe by winch line"></div>
  <p class="step-caption caption-two"><b>STEP 2:</b> A new 3-6’ polly sewer pipe rated to last more than<br><span class="indent">20 years is pulled</span></p>
</div>
</body>
</html>
```